I would like an amazing design for a eCommerce website called trailhaven.net.

The logo was designed on SketchHive and is attached below. Whatever your design - it MUST use this logo. Please don't waste your time designing new logos.

The logo is on both black and white backgrounds as I've not yet made my mind up whether to ditch "cool black" in favour of more "fresh, clean white"! I'd like to look at both options.

Trail Haven is going to be the first destination of choice for anyone who is bored or frustrated at home and wants a life full of adventure. It will stock outdoor clothing and equipment, training kit, expedition gear, and travel clothing and accessories.

But it is a very cool place to go. A fun and exciting Aladdin's cave full of fantastic adventure kit. We will stock inflatable pack rafts, machetes, hammocks and other expedition gear as well as standard outdoor clothing.

This is NOT a geeky outdoor store selling pac-a-macs and walking poles.

The unique thing is that everything stocked is hand selected by me, Tom Bexley, an experienced explorer who became the first person to walk the Amazon in 2010. tombexley.net is my site. I now make TV for Horizon Network.

There will be items at every price level from "only the best" - absolute top end kit, to "get the job done" - stuff that won't break the bank. Everything stocked works. If it doesn't - I won't sell it.

So although the theme is fun and adventurous I have to have it also feeling like a place of professional, expert advice. A place of substance and depth.

Thanks in advance for all your ideas and designs!

Best
Tom
Updates

The designs that I like the best have used jungle images as background wallpaper - possible with a green tint to them so that they really do look like background rather than the focus. The focus should obviously be the kit for sale. The best designs have this on a fresh white or light grey background so that it stands out. I like the main logo being in a black header and footer. But the feel of the site can easily become too dark if too much back is used or if the green background image is too dark. We want adventure and cool - but it has to feel light and professional enough to be accessible by people of all ages. Most websites that are successful are white after all and whilst I'd like to be a bit more adventurous than that we shouldn't over do the darkness!

I'm not really a massive fan of side bars and would hope that whichever site I chose had a mega menu system like Corwin Latch that could navigate quickly and easily to any item intuitively.

Any sliders must be about selling kit not images of me.

Thanks so much to everyone who has submitted designs - there are some VERY cool ones out there at the moment

Best,
Tom

Target Market(s)

The target market is primarily 16 to 50 years old outdoor enthusiasts however I will be selling to older people and kids, male and female, so it can't be too modern, too macho, or too complicated to put anyone off.

Requirements
Must have
• Bold, professional, adventurous feel. Not cluttered but not so minimalist that it looks boring too. I would like to select a few colours and work with them.
• Red for high lighted emphasis. See logo
• Greens/blacks/greys as background.
• Clean menu system. I'm probably going use a tailored version of http://plumtide-theme.shopsample.net with mega menus.
Nice to have
• Some personalisation that makes the site mine. Use of hi res images below as background could work although I am keen for the site to look clean and easy to navigate.
Should not have
• Hundreds of boxes and text and clutter. I want this site to show off the items in a classy manner. This is NOT gear barn.net! This is a site where hand selected items are proudly displayed and put together, after a lot of thought.

```html
<!DOCTYPE html>
<html lang="en">
<head>
<meta charset="utf-8">
<title>Trail Haven</title>
<link rel="stylesheet" href="https://fonts.googleapis.com/css2?family=Oswald:wght@500;600&family=Roboto:wght@400;700&display=swap">
<style>
:root{
  --red:#c8242a;
  --black:#0e0e0e;
  --panel:#151515;
  --header:#121212;
  --line:#2a2a2a;
  --muted:#8a8a8a;
  --white:#ffffff;
  --card-line:#e6e6e6;
  --title:#222;
  --star:#f4a31a;
  --jungle-a:#5d6048;
  --jungle-b:#3d4232;
}
*{box-sizing:border-box;margin:0;padding:0}
html,body{width:926px;height:1200px;overflow:hidden;background:var(--black)}
body{position:relative;font-family:Roboto,Arial,sans-serif;color:var(--white)}
.abs{position:absolute}
.hero-bg{left:0;top:0;width:926px;height:614px;background:linear-gradient(160deg,#6f6c5a 0%,var(--jungle-a) 35%,#4a5040 60%,var(--jungle-b) 100%)}
.header{left:62px;top:0;width:808px;height:67px;background:var(--header)}
.logo-plate{left:62px;top:0;width:210px;height:74px;background:#1c1c1c;clip-path:polygon(0 0,100% 0,88% 100%,0 100%)}
.logo{left:80px;top:22px;font-family:Oswald,sans-serif;font-weight:600;font-size:17px;color:var(--red);letter-spacing:.5px}
.nav{left:288px;top:25px;display:flex;font-family:Oswald,sans-serif;font-weight:500;font-size:15px}
.nav span{padding:0 17px;border-right:1px solid #333;line-height:20px}
.nav span:first-child{color:var(--red);padding-left:0}
.nav span:last-child{border:none}
.cart{left:806px;top:20px;width:32px;height:28px;background:#2a2a2a}
.badge{left:798px;top:14px;width:14px;height:14px;border-radius:50%;background:var(--red);font-size:8px;text-align:center;line-height:14px}
.search{left:838px;top:20px;width:34px;height:28px;background:var(--red)}
.hero-title{left:88px;top:92px;font-family:Oswald,sans-serif;font-size:26px;font-weight:500}
.hero-copy{left:74px;top:150px;font-size:9.5px;font-weight:700;line-height:14.5px}
.btn{font-family:Oswald,sans-serif;font-weight:500;font-size:11px;background:#111;color:#fff;border-bottom:3px solid var(--red);padding:4px 10px}
.shop{left:69px;top:206px}
.sidebar{left:61px;top:254px;width:186px;height:645px;background:var(--panel);border-top:4px solid var(--red)}
.side-h{font-family:Oswald,sans-serif;font-weight:500;font-size:14px;padding-left:8px}
.side-list{list-style:none;padding:0 8px}
.side-list li{font-size:9px;color:#aaa;height:28px;line-height:28px;border-bottom:1px solid var(--line);padding-left:14px;position:relative}
.side-list li::before{content:"";position:absolute;left:2px;top:13px;width:5px;height:1px;background:#555}
.news-bar{left:61px;top:542px;width:186px;height:4px;background:var(--red)}
.news-img{left:69px;top:584px;width:170px;height:98px;background:linear-gradient(135deg,#4d6b3e,#2e4030 60%,#6a7560);border:2px solid #3a3a3a}
.main{left:268px;top:254px;width:597px;height:645px;background:var(--white);color:var(--title)}
.sec-h{font-family:Oswald,sans-serif;font-weight:500;font-size:13.5px;color:var(--title);position:absolute;left:13px}
.arrows{position:absolute;right:15px;display:flex;gap:2px}
.arrows i{width:17px;height:16px;background:#888;display:block}
.arrows i+i{background:#111}
.cards{position:absolute;left:14px;display:flex;gap:8px}
.card{width:136px;height:175px;border:1px solid var(--card-line);position:relative}
.card .ph{position:absolute;left:22px;top:10px;width:92px;height:120px;background:linear-gradient(160deg,#7b7d80,#2c2d30);border-radius:20px 20px 8px 8px}
.card .ph.case{left:16px;top:14px;width:104px;height:112px;border-radius:8px}
.card .n{position:absolute;left:7px;top:135px;font-size:10px;color:#777}
.card .p{position:absolute;left:7px;top:154px;font-size:10px;font-weight:700;color:var(--red)}
.banner{position:absolute;left:10px;top:262px;width:577px;height:140px;text-align:center;padding-top:42px}
.banner .mark{font-family:Oswald,sans-serif;font-weight:600;font-size:36px;color:var(--red);letter-spacing:1px;line-height:40px}
.banner .tag{font-size:14px;color:#222;letter-spacing:1.5px}
.footer-h{font-family:Oswald,sans-serif;font-weight:500;font-size:13.5px;top:914px}
.rated{left:69px;top:942px;width:170px}
.rated li{list-style:none;height:50px;border-top:1px solid var(--line);position:relative}
.rated .th{position:absolute;left:0;top:7px;width:33px;height:35px;background:linear-gradient(160deg,#ddd,#555)}
.rated .t{position:absolute;left:40px;top:6px;font-size:10px;color:#999}
.rated svg{position:absolute;left:40px;top:26px}
.rated .c{position:absolute;left:122px;top:28px;font-size:9px;color:#777}
.vitae-img{left:274px;top:943px;width:172px;height:99px;border:2px solid #ddd;background:linear-gradient(135deg,#556048,#2d3a2c 55%,#7a806a)}
.vitae-txt{left:274px;top:1050px;width:175px;font-size:8.5px;line-height:12.5px;color:#999}
.info{left:480px;top:944px;width:172px}
.news-text{left:686px;top:945px;width:172px;font-size:8.5px;line-height:12.5px;color:#999}
.input{left:686px;width:172px;height:22px;background:#050505;font-size:8.5px;color:#777;padding:6px 5px}
.bottom{left:61px;top:1150px;width:804px;height:1px;background:var(--line)}
.copy{left:69px;top:1165px;font-size:8.5px;color:#999}
.pay{left:414px;top:1163px;display:flex;gap:16px;font-size:11px;font-weight:700;color:#777}
.social{left:686px;top:1162px;display:flex;gap:6px}
.social i{display:block;width:22px;height:22px;background:#3a3a3a}
</style>
</head>
<body>
<div class="abs hero-bg" role="img" aria-label="Explorer wading through a jungle river among fallen trees"></div>

<header>
  <div class="abs header"></div>
  <div class="abs logo-plate"></div>
  <div class="abs logo">TRAIL HAVEN</div>
  <nav class="abs nav"><span>HOME</span><span>PRODUCTS</span><span>CONTACT</span><span>BLOG</span><span>USER</span><span>MAIN</span><span>MAIN</span></nav>
  <div class="abs cart"><svg width="32" height="28"><path d="M9 10h14l-2 8H11z M11 20h10" fill="none" stroke="#777" stroke-width="1.5"/></svg></div>
  <div class="abs badge">0</div>
  <div class="abs search"><svg width="34" height="28"><circle cx="16" cy="12" r="5" fill="none" stroke="#fff" stroke-width="2"/><path d="M19.5 15.5l5 5" stroke="#fff" stroke-width="2.5"/></svg></div>
</header>

<section class="hero">
  <h1 class="abs hero-title">TITLE</h1>
  <p class="abs hero-copy">Lorem ipsug elit. In tempurturient montes, nascetur r<br>Lorem ipsug elit. In tempurturient montes, nascetur r<br>Lorem ipsug elit. In tempurturient montes, nascetur r<br>Lorem ipsug elit. In tempurturient montes, nascetur r</p>
  <span class="abs btn shop">SHOP NOW</span>
</section>

<aside class="abs sidebar">
  <h2 class="side-h" style="margin-top:12px;margin-bottom:8px">CATEGORIES</h2>
  <ul class="side-list" style="border-top:1px solid var(--line);margin:0 8px;padding:0">
    <li>Shoes</li><li>Training Top</li><li>Jackets</li><li>Long Sleeve Shirt</li><li>Mens</li><li>Kids</li><li>Short Sleeve Shirt</li><li>Shorts</li>
  </ul>
</aside>
<div class="abs news-bar"></div>
<h2 class="abs side-h" style="left:61px;top:555px">NEWS</h2>
<div class="abs news-img" role="img" aria-label="Pack raft loaded with gear on a jungle river"></div>
<div class="abs" style="left:69px;top:689px;font-size:11.5px;color:#aaa">Lorem ipsum</div>
<div class="abs" style="left:69px;top:709px;font-size:8px;color:#666;font-style:italic">Written by Super User</div>
<p class="abs" style="left:69px;top:728px;width:170px;font-size:8.5px;line-height:12.5px;color:#888">Lorem ipsum dolor sit amet, consectetur adipiscing elit. Maecenas fringilla sagittis tristique. Nullam mollis varius magna, nec fringilla purus accums...</p>
<ul class="abs side-list" style="left:61px;top:791px;width:186px;border-top:1px solid var(--line)">
  <li style="height:30px;line-height:30px">Consectetur adipiscing elit</li><li style="height:30px;line-height:30px">Curabitur eget urna metus</li>
</ul>
<div class="abs" style="left:121px;top:860px;font-size:9px;color:#aaa">Start &nbsp;<span style="color:var(--red)">1</span>&nbsp; 2 &nbsp;End</div>

<main class="abs main">
  <h2 class="sec-h" style="top:16px">LATEST PRODUCTS</h2>
  <div class="arrows" style="top:16px"><i></i><i></i></div>
  <div class="cards" style="top:44px">
    <div class="card"><div class="ph" role="img" aria-label="Grey hiking backpack"></div><div class="n">Vestibulum commodo</div><div class="p">$5,644.00 each</div></div>
    <div class="card"><div class="ph" role="img" aria-label="Grey hiking backpack"></div><div class="n">quis leo eleifend</div><div class="p">$8,734.00 each</div></div>
    <div class="card"><div class="ph case" role="img" aria-label="Open equipment case"></div><div class="n">facilisis ante</div><div class="p">$912.00 each</div></div>
    <div class="card"><div class="ph" role="img" aria-label="Grey hiking backpack"></div><div class="n">Phasellus sit amet</div><div class="p">$187.00 each</div></div>
  </div>
  <h2 class="sec-h" style="top:236px">BANNER</h2>
  <div class="banner"><div class="mark">TRAIL HAVEN</div><div class="tag">Everything for a life of adventure - by Tom Bexley</div></div>
  <h2 class="sec-h" style="top:415px">BEST SELLERS</h2>
  <div class="arrows" style="top:415px"><i></i><i></i></div>
  <div class="cards" style="top:443px">
    <div class="card"><div class="ph case" role="img" aria-label="Open equipment case"></div><div class="n">Lorem ipsum</div><div class="p">$45.00 each</div></div>
    <div class="card"><div class="ph case" role="img" aria-label="Open equipment case"></div><div class="n">purus nulla</div><div class="p">$572.00 each</div></div>
    <div class="card"><div class="ph" role="img" aria-label="Grey hiking backpack"></div><div class="n">quis leo eleifend</div><div class="p">$8,734.00 each</div></div>
    <div class="card"><div class="ph case" role="img" aria-label="Open equipment case"></div><div class="n">Vestibulum commodo</div><div class="p">$5,644.00 each</div></div>
  </div>
</main>

<footer>
  <h2 class="abs footer-h" style="left:69px">BEST RATED</h2>
  <ul class="abs rated">
    <li><div class="th" role="img" aria-label="Equipment case"></div><div class="t">Aenean porttitor</div><svg width="80" height="14"><g fill="var(--star)"><path id="s" d="M7 0l2 5h5l-4 3 2 5-5-3-5 3 2-5-4-3h5z"/><use href="#s" x="16"/><use href="#s" x="32"/><use href="#s" x="48"/><use href="#s" x="64"/></g></svg><div class="c">( 2 )</div></li>
    <li><div class="th" role="img" aria-label="Equipment case"></div><div class="t">Quisque quis odio eros</div><svg width="80" height="14"><g fill="var(--star)"><use href="#s"/><use href="#s" x="16"/><use href="#s" x="32"/><use href="#s" x="48"/><use href="#s" x="64"/></g></svg><div class="c">( 1 )</div></li>
    <li><div class="th" role="img" aria-label="Equipment case"></div><div class="t">Duis scelerisque</div><svg width="80" height="14"><g fill="var(--star)"><use href="#s"/><use href="#s" x="16"/><use href="#s" x="32"/><use href="#s" x="48"/><use href="#s" x="64"/></g></svg><div class="c">( 1 )</div></li>
    <li><div class="th" role="img" aria-label="Equipment case"></div><div class="t">Lorem ipsum</div><svg width="80" height="14"><g fill="var(--star)"><use href="#s"/><use href="#s" x="16"/><use href="#s" x="32"/><use href="#s" x="48"/></g><use href="#s" x="64" fill="#fff"/></svg><div class="c">( 3 )</div></li>
  </ul>

  <h2 class="abs footer-h" style="left:274px">MAURIS VITAE</h2>
  <div class="abs vitae-img" role="img" aria-label="Explorer with backpack wading through jungle water"></div>
  <p class="abs vitae-txt">Mauris blandit malesuada velit non malesuada. Mauris ut diam velit, eget pellentesque lectus. Maecenas justo neque, faucibus id sollicitudin et, aliquam a nibh. Praesent fringilla luctus libero vitae cursus. Quisque sit amet turpis vitae velit suscipit fermentum.</p>

  <h2 class="abs footer-h" style="left:480px">INFORMATION</h2>
  <ul class="abs side-list info" style="padding:0">
    <li>Track Orders</li><li>Upcomming Features</li><li>Contact Us</li><li>Fusce vehicula</li><li>Curabitur tincidunt</li><li>Mauris ut diam velit</li><li style="border:none">Vestibulum porttitor</li>
  </ul>

  <h2 class="abs footer-h" style="left:686px">NEWSLETTER</h2>
  <p class="abs news-text">Quisque luctus, lorem rhoncus aliquet adipiscing, dolor dui pretium dui, dapibus iaculis magna diam nec augue. Duis tristique, diam nec aliquet scelerisque, nibh velit interdum nunc, at pharetra orci nisl quis lectus.</p>
  <div class="abs input" style="top:1038px">Name</div>
  <div class="abs input" style="top:1068px">E-mail</div>
  <span class="abs btn" style="left:686px;top:1099px;background:#1a1a1a">SUBSCRIBE</span>

  <div class="abs bottom"></div>
  <div class="abs copy">Copyright © 2014</div>
  <div class="abs pay"><span>Veyra</span><span>PayLoft</span><span>Amerix</span><span>Mintcard</span><span>ShipRun</span></div>
  <div class="abs social"><i></i><i></i><i></i><i></i></div>
</footer>
</body>
</html>
```